Business Cards - Brightwell Harbor

need to design unique business card for my mortgage business. I need to design credit card style business card for my business or any unique idea that you might have

Target Market(s)

Home Loan customers

Industry/Entity Type

Mortgage Brokerage

Contact Information for Business Card

please design credit card style or very unique style business card

Colors

Designer to choose colors to be used in the design.

Requirements
Must have
• Name
• position
• Phone number
• fax number
• email address
• website address
• social media address
• All above fields will be provided once design in finalised

```html
<!DOCTYPE html>
<html lang="en">
<head>
<meta charset="utf-8">
<title>Brightwell Harbor Business Card</title>
<link href="https://fonts.googleapis.com/css2?family=Roboto:wght@400;500;700&family=Roboto+Condensed:wght@700&display=swap" rel="stylesheet">
<style>
  :root {
    --backdrop: #2a2a2a;
    --card-white: #f1f1f1;
    --brand-blue: #0b2fc6;
    --brand-deep: #0a2ec4;
    --accent-orange: #f7891f;
    --text-grey: #4a4a4a;
    --white: #ffffff;
  }
  * { margin: 0; padding: 0; box-sizing: border-box; }
  html, body {
    width: 1200px; height: 960px; overflow: hidden;
    background: var(--backdrop);
    font-family: "Roboto", Arial, sans-serif;
  }
  .canvas { position: relative; width: 1200px; height: 960px; }

  .card {
    position: absolute; width: 600px; height: 343px;
    box-shadow: 0 3px 8px rgba(0,0,0,.45);
  }
  .card-front { left: 314px; top: 113px; background: var(--card-white); }
  .card-back { left: 311px; top: 472px; background: var(--brand-deep); }

  .edge-bar { position: absolute; top: 74px; width: 11px; height: 194px; }
  .edge-bar.left { left: 0; background: var(--brand-blue); }
  .edge-bar.right { right: 0; background: var(--accent-orange); }

  .contact { position: absolute; left: 28px; top: 80px; color: var(--text-grey); }
  .contact-name {
    font-family: "Roboto Condensed", "Roboto", sans-serif;
    font-weight: 700; font-size: 21px; color: var(--brand-blue); line-height: 24px;
  }
  .contact-role { font-size: 15px; font-weight: 500; color: var(--accent-orange); margin-top: 3px; }
  .contact-address { font-size: 14.5px; line-height: 19px; margin-top: 14px; }
  .contact-lines { list-style: none; margin-top: 10px; font-size: 14.5px; }
  .contact-lines li { display: flex; align-items: center; height: 19px; }
  .contact-lines svg { width: 13px; height: 13px; margin-right: 10px; fill: var(--brand-blue); }

  .brand-lockup {
    position: absolute; display: flex; align-items: center; justify-content: center;
    gap: 10px; white-space: nowrap;
  }
  .card-front .brand-lockup { left: 336px; top: 154px; width: 240px; height: 36px; }
  .card-back .brand-lockup { left: 150px; top: 152px; width: 300px; height: 42px; }
  .brand-dot { width: 16px; height: 16px; border-radius: 50%; flex: none; }
  .brand-name { font-weight: 700; }
  .card-front .brand-dot { background: var(--accent-orange); }
  .card-front .brand-name { color: var(--brand-blue); font-size: 25px; line-height: 36px; }
  .card-back .brand-dot { background: var(--white); width: 18px; height: 18px; }
  .card-back .brand-name { color: var(--white); font-size: 30px; line-height: 42px; }

  .social-row {
    position: absolute; left: 0; right: 0; top: 290px;
    display: flex; justify-content: center; align-items: center;
  }
  .social-rule { width: 165px; height: 1px; }
  .social-rule.left { background: linear-gradient(to right, rgba(255,255,255,0), rgba(255,255,255,.9)); margin-right: 9px; }
  .social-rule.right { background: linear-gradient(to left, rgba(255,255,255,0), rgba(255,255,255,.9)); margin-left: 9px; }
  .social-dots { display: flex; gap: 5px; }
  .social-dots span { width: 28px; height: 28px; border-radius: 50%; background: var(--white); }
</style>
</head>
<body>
<main class="canvas">
  <section class="card card-front">
    <div class="edge-bar left"></div>
    <div class="edge-bar right"></div>
    <div class="contact">
      <h1 class="contact-name">DANIEL REYES</h1>
      <p class="contact-role">CEO/FOUNDER</p>
      <p class="contact-address">2145 Alder Crest Way<br>Fairbanks, Alaska 39812</p>
      <ul class="contact-lines">
        <li><svg viewBox="0 0 16 16"><path d="M3.6 1.2l2.3 2.6-1.2 1.9c.9 2 2.6 3.7 4.6 4.6l1.9-1.2 2.6 2.3-1.2 2.4c-5.6-.4-10.4-5.2-10.8-10.8z"/></svg>555 204 7719</li>
        <li><svg viewBox="0 0 16 16"><path d="M4 1h7l1 1v3H4zM1 6h14v6h-2v3H3v-3H1zm4 5v3h6v-3z"/></svg>555 318 6042</li>
        <li><svg viewBox="0 0 16 16"><path d="M1 3h14v10H1zm1.5 1.5v.3L8 9l5.5-4.2v-.3z"/></svg>hello@brightwellharbor.com</li>
        <li><svg viewBox="0 0 16 16"><path d="M8 1a7 7 0 100 14A7 7 0 008 1zm-1 2.2c-.5 1 .6 1.6.2 2.5-.5.9-2.2.4-2.4 1.6-.2 1.1 1.4 1.3 1.6 2.4.2 1-.4 2.2.4 2.8A5.1 5.1 0 017 3.2zm3 .4c1.8.8 3 2.5 3 4.4-.7-.4-1.5-.1-1.9.6-.5.8.1 2-.7 2.5-.6.3-1.3-.5-1.1-1.3.2-.9-.8-1.3-.6-2.2.2-.8 1.3-.6 1.4-1.5.1-.9-.3-1.7-.1-2.5z"/></svg>www.brightwellharbor.com</li>
      </ul>
    </div>
    <div class="brand-lockup">
      <span class="brand-dot"></span><span class="brand-name">Brightwell Harbor</span>
    </div>
  </section>

  <section class="card card-back">
    <div class="brand-lockup">
      <span class="brand-dot"></span><span class="brand-name">Brightwell Harbor</span>
    </div>
    <div class="social-row">
      <div class="social-rule left"></div>
      <div class="social-dots"><span></span><span></span><span></span><span></span></div>
      <div class="social-rule right"></div>
    </div>
  </section>
</main>
</body>
</html>
```